TFP Tarlo Fluid Power company brochure

We need the design of brochure of a company that provides consultancy, design and supply of key equipment in the field of Wastewater, clean water, organic waste anaerobic treatment and green energy production for Industries. The attached files are:
TFP wording in english that describes activities
Some drawings (useful for design)
Presentation (in italian)
It would be nice to have a 4 pages brochure possibly in double language (english and italian).

Target Market(s)

water and waste

Industry/Entity Type

It Company

Colors

Designer to choose colors to be used in the design.

Requirements
Must have
• use the logo TFP as per attached docs

```html
<!DOCTYPE html>
<html lang="en">
<head>
<meta charset="utf-8">
<title>TFP Tarlo Fluid Power – Brochure</title>
<link rel="stylesheet" href="https://fonts.googleapis.com/css2?family=Oswald:wght@400;500;600&family=Lato:wght@400;700&display=swap">
<style>
  :root{
    --bg:#e6e6e6;
    --orange:#f0611c;
    --blue-head:#1a5f9e;
    --crimson:#d0123f;
    --green:#3aa63a;
    --ink:#2a2a2a;
    --white:#ffffff;
    --dark:#3b3b3d;
  }
  *{box-sizing:border-box;margin:0;padding:0}
  html,body{width:1200px;height:1200px;overflow:hidden;background:var(--bg)}
  body{position:relative;font-family:"Lato",sans-serif;color:var(--ink)}
  .spread{position:absolute;left:194px;width:813px;height:580px;overflow:hidden;background:var(--white)}
  .spread--cover{top:8px}
  .spread--inside{top:608px}
  .abs{position:absolute}

  /* cover left */
  .cover-back{left:0;top:0;width:407px;height:580px;
    background:linear-gradient(180deg,#d8d8d8 0%,#b9b9b9 35%,#8e8e8e 55%,#6a6a6a 75%,#3b3b3d 100%)}
  .cover-circle{border-radius:50%;border:4px solid var(--white);
    background:radial-gradient(circle at 40% 40%,#a4a78d,#6e7160)}
  .circle-a{left:112px;top:38px;width:140px;height:140px;background:radial-gradient(circle at 50% 40%,#7da050,#b9a582 60%,#8f8a70)}
  .circle-b{left:234px;top:14px;width:104px;height:104px;background:radial-gradient(circle at 50% 40%,#c4cbd2,#5a5f62)}
  .circle-c{left:214px;top:134px;width:100px;height:100px;background:radial-gradient(circle at 50% 50%,#dfe2e6,#8b9098)}
  .brand-mark{left:66px;top:394px;display:flex;align-items:center;gap:8px}
  .brand-dot{width:22px;height:22px;border-radius:50%;background:var(--orange)}
  .brand-name{font-family:"Oswald",sans-serif;font-weight:500;font-size:17px;color:var(--white)}
  .contacts{left:66px;top:498px;color:var(--white);font-family:"Oswald",sans-serif;list-style:none}
  .contacts li{display:flex;align-items:center;gap:8px;line-height:1.3}
  .contacts .big{font-size:11px;font-weight:500}
  .contacts .small{font-size:7.5px}
  .contacts svg{width:8px;height:8px;flex:none}

  /* cover right */
  .cover-front{left:407px;top:0;width:406px;height:580px;
    background:linear-gradient(180deg,#9c92d8 0%,#c9a6c8 22%,#f2b47a 40%,#f6a53a 47%,#4d4a4a 52%,#8d8590 62%,#6f6a72 78%,#3b3b3d 100%)}
  .logo-box{left:578px;top:16px;width:235px;height:70px;background:var(--white);
    display:flex;align-items:center;justify-content:center;gap:10px}
  .logo-box .brand-name{color:var(--blue-head);font-size:20px}
  .logo-box .brand-dot{width:26px;height:26px}
  .cover-title{right:64px;top:488px;text-align:right}
  .cover-title h1{font-family:"Oswald",sans-serif;font-weight:600;font-size:26px;color:var(--orange);letter-spacing:.3px}
  .cover-title p{font-family:"Oswald",sans-serif;font-weight:400;font-size:12px;color:var(--white);line-height:1.4}

  /* inside */
  .band{top:0;height:190px;width:407px}
  .band--blue{left:0;background:linear-gradient(135deg,#2a5f82,#2b7db3 50%,#1c4e72)}
  .band--orange{left:407px;width:406px;background:linear-gradient(135deg,#c24a10,#ef6a22 45%,#b8430c)}
  .band-title{font-family:"Oswald",sans-serif;font-weight:500;font-size:18px;color:var(--white)}
  .band-title--left{left:64px;top:166px}
  .band-title--right{left:472px;top:160px}
  .bullets{list-style:none;font-size:8px;line-height:1.3}
  .bullets li{position:relative;padding-left:18px;margin-bottom:3.5px}
  .bullets li::before{content:"";position:absolute;left:0;top:2px;width:4px;height:4px;border-radius:50%;background:var(--green)}
  .provide{left:64px;top:212px;width:260px}
  .why-title{left:64px;top:344px;font-family:"Oswald",sans-serif;font-weight:500;font-size:18px;color:var(--blue-head)}
  .why-text{left:64px;top:379px;width:280px;font-size:8px;line-height:1.3}
  .why-list{left:64px;top:414px;width:282px}
  .tech{left:472px;top:210px;width:280px;list-style:none}
  .tech > li{margin-bottom:8px}
  .tech-head{display:flex;gap:9px;font-size:10.5px;color:var(--crimson)}
  .tech-head b{color:var(--ink);font-weight:700}
  .tech ol{list-style:none;margin:7px 0 0 19px;font-size:7.6px;line-height:1.3}
  .tech ol li{display:flex;gap:10px;margin-bottom:3px}
  .tech ol span{width:8px;flex:none}
  .plant{left:24px;top:494px;width:789px;height:86px;
    background:linear-gradient(180deg,rgba(235,235,235,0) 0%,#ececec 40%,#e0e0e0 100%)}
</style>
</head>
<body>

<section class="spread spread--cover" aria-label="Brochure cover spread">
  <div class="abs cover-back" role="img" aria-label="Black and white photo of a circular clarifier bridge over still water"></div>
  <div class="abs cover-circle circle-a" role="img" aria-label="Round photo of a treatment plant with walkways in a green field"></div>
  <div class="abs cover-circle circle-b" role="img" aria-label="Round photo of a digester tank"></div>
  <div class="abs cover-circle circle-c" role="img" aria-label="Round photo of stainless steel silos"></div>

  <div class="abs brand-mark"><span class="brand-dot"></span><span class="brand-name">TFP Tarlo Fluid Power</span></div>

  <ul class="abs contacts">
    <li class="big"><svg viewBox="0 0 10 10"><path d="M2 1l2 2-1 1.2c.6 1.2 1.6 2.2 2.8 2.8L7 6l2 2-1.3 1.3C4.5 9 1 5.5.7 2.3z" fill="#fff"/></svg>011.5550182</li>
    <li class="big"><svg viewBox="0 0 10 10"><rect x="3" y="0.5" width="4" height="9" rx="0.8" fill="none" stroke="#fff"/></svg>333 555 0147</li>
    <li class="small" style="margin-top:3px"><svg viewBox="0 0 10 10"><rect x="1" y="2.5" width="8" height="5" fill="#fff"/></svg>INFO@TFP-FLUID.EXAMPLE</li>
    <li class="small" style="margin-top:6px"><svg viewBox="0 0 10 10"><path d="M5 9.5S1.8 6 1.8 4a3.2 3.2 0 016.4 0c0 2-3.2 5.5-3.2 5.5z" fill="#fff"/></svg>TFP SRL - VIA DELLE ROGGE 18 - ITALY</li>
    <li class="small" style="padding-left:16px">PIVA: 12345670019</li>
  </ul>

  <div class="abs cover-front" role="img" aria-label="Sunset photo over clarifier tanks at a water treatment plant"></div>
  <div class="abs logo-box"><span class="brand-dot"></span><span class="brand-name">Tarlo Fluid Power</span></div>
  <div class="abs cover-title">
    <h1>COMPLETE SOLUTION FOR</h1>
    <p>Waste minimization, watewaters water &amp; Products<br>recovery and energy in industry</p>
  </div>
</section>

<section class="spread spread--inside" aria-label="Brochure inside spread">
  <div class="abs band band--blue" role="img" aria-label="Blue tinted photo of a rotating drum screen over sludge"></div>
  <div class="abs band band--orange" role="img" aria-label="Orange tinted photo of a domed biogas digester"></div>
  <h2 class="abs band-title band-title--left">WE PROVIDE:</h2>
  <h2 class="abs band-title band-title--right">PROPOSED TECHNOLOGIES:</h2>

  <div class="abs plant" role="img" aria-label="Line drawing of plant buildings and storage tanks"></div>

  <ul class="abs bullets provide">
    <li>Feasibility studies</li>
    <li>Pilot ttest with our internal labs</li>
    <li>Process design (over 240 plants successfully executed and running)</li>
    <li>Basic and detailed engineering</li>
    <li>Key equipment support</li>
    <li>Construction and start-up supervision</li>
    <li>Operation and supervision expertise (more than 20 years of internal expertise of various biological and chemical reactions)</li>
  </ul>

  <h2 class="abs why-title">WHY TO CHOOSE US ?</h2>
  <p class="abs why-text">TFP ltd (TFP) has the mission to solve any client's environmental problem with best process solution available on the market, most reliable and economical both on the CAPEX and OPEX.</p>
  <ul class="abs bullets why-list">
    <li>Cost reduction: TFP first identify the inefficient processes and remove them.</li>
    <li>Only when the emission reduction is not any more possible or economically feasible, TFP propose the best treatment to the client.</li>
    <li>TFP provide best solutions on a variety of biological and chemical processes</li>
    <li>TFP provide highly qualified and independent consultancy</li>
  </ul>

  <ol class="abs tech">
    <li>
      <div class="tech-head"><b>1.</b>Biological processes:</div>
      <ol>
        <li><span>a.</span>Oxidation, nitrification, denitrification, P-removal</li>
        <li><span>b.</span>N-recovery and slow release fertilizers production</li>
        <li><span>c.</span>Anaerobic processes: UASB, Food waste, odour removal</li>
        <li><span>d.</span>Metal recovery</li>
      </ol>
    </li>
    <li><div class="tech-head"><b>2.</b>High value products recovery</div></li>
    <li>
      <div class="tech-head"><b>3.</b>Chemical/Phisical processes:</div>
      <ol>
        <li><span>a.</span>Flotation DAF</li>
        <li><span>b.</span>Filtration and membrane filtration</li>
        <li><span>c.</span>Chemical oxidations / reductions (e.g. Fenton, color removal, CN, Cr6+ removal ....)</li>
        <li><span>d.</span>Disinfection</li>
      </ol>
    </li>
    <li><div class="tech-head"><b>4.</b>Water recovery and recycle</div></li>
  </ol>
</section>

</body>
</html>
```